QuillaVorn needs a dashboard page designed

Redesign the dashboard shown in the provided images.

There are two images:
- dashboard.png
- dashboard-expanded.png

NOTE: The vocabulary navigation on the left will be a very long list of words 100s, so keep that in mind when you're designing both the vocab navigation and the expanded vocab popup.

In the dashboard.png picture, there needs to be a progress chart showing the word progress like the following: review 1(show it as completed) -> review 2(show the user they are here) -> review 3(unvisited) -> review 4(unvisited)

The do-not-design-this-page.png image is for your reference only. It is not to be designed. Use it to understand the overall look and feel of the website to help you create the best dashboard page possible.
Updates

Need extra days to review

Industry/Entity Type

Education English learning

Number of Pages Required

1 page

Requirements
Must have
• The main navigation and main header cannot change between pages. See the do-not-design page for the main navigateion and header.
Should not have
• Do not add a person profile. We will not have images of our users. Keep the icons in the main navigation as they are.

```html
<!DOCTYPE html>
<html lang="en">
<head>
<meta charset="utf-8">
<title>QuillaVorn – Vocabulary Dashboard</title>
<link rel="stylesheet" href="https://fonts.googleapis.com/css2?family=Nunito+Sans:wght@400;600;700;800&family=Arimo:wght@400;700&display=swap">
<style>
  :root {
    --page-bg: #f7f7f7;
    --shell: #3c434c;
    --panel: #2e343b;
    --card: #ffffff;
    --ink: #2b2b2b;
    --ink-soft: #3a3a3a;
    --nav-text: #c9cdd2;
    --nav-strong: #ffffff;
    --accent: #4a87c9;
    --pill-bg: #3d444c;
    --step-done: #4a87c9;
    --step-idle: #b9bcc0;
    --step-line: #c9cbce;
    --band-long: #e8eff8;
    --band-working: #edf5ed;
    --band-short: #fdfbea;
    --band-forgotten: #f2f2f2;
    --bar: #2b61b1;
    --star: #f7b924;
  }
  * { box-sizing: border-box; margin: 0; padding: 0; }
  html, body { width: 1200px; height: 819px; overflow: hidden; }
  body {
    background: var(--page-bg);
    font-family: "Nunito Sans", Arial, sans-serif;
    position: relative;
  }
  .app-shell {
    position: absolute; left: 61px; top: 61px; width: 1078px; height: 697px;
    background: var(--shell); border-radius: 25px; overflow: hidden;
    box-shadow: 0 10px 40px rgba(0,0,0,.08);
  }
  .app-header { position: absolute; left: 0; top: 0; width: 100%; height: 62px; }
  .menu-toggle { position: absolute; left: 30px; top: 24px; }
  .app-title {
    position: absolute; left: 0; right: 0; top: 23px; text-align: center;
    color: #e6e8eb; font-size: 9.5px; font-weight: 600; letter-spacing: .1px;
  }
  .app-title svg { vertical-align: middle; margin-left: 3px; }
  .header-actions { position: absolute; right: 34px; top: 22px; display: flex; gap: 12px; align-items: center; }

  .main-nav { position: absolute; left: 0; top: 102px; width: 129px; }
  .main-nav__item {
    display: flex; align-items: center; gap: 8px;
    height: 37px; padding-left: 18px; margin-left: 13px;
    color: var(--nav-text); font-size: 9px; font-weight: 600; margin-bottom: 3px;
  }
  .main-nav__item--active {
    background: var(--panel); color: var(--nav-strong); font-weight: 700;
    border-radius: 18px 0 0 18px;
  }

  .work-panel {
    position: absolute; left: 129px; top: 62px; right: 0; bottom: 0;
    background: var(--panel); border-top-left-radius: 25px;
  }
  .vocab-tools { position: absolute; left: 13px; top: 77px; display: flex; gap: 8px; }
  .deck-select {
    width: 78px; height: 27px; border-radius: 14px; background: var(--pill-bg);
    display: flex; align-items: center; padding: 0 10px 0 12px; gap: 5px;
    color: #e6e8eb; font-size: 9px; font-weight: 600;
  }
  .deck-select .chev { margin-left: auto; }
  .popout-btn {
    width: 33px; height: 27px; border-radius: 14px; background: var(--pill-bg);
    display: flex; align-items: center; justify-content: center;
  }
  .stage-tab {
    position: absolute; left: 13px; top: 126px; width: 133px; height: 37px;
    background: var(--card); border-radius: 18px 0 0 18px;
    display: flex; align-items: center; gap: 5px; padding-left: 15px;
    color: var(--ink); font-size: 9px; font-weight: 700;
  }
  .vocab-list { position: absolute; left: 38px; top: 176px; list-style: none; }
  .vocab-list li {
    position: absolute; left: 0; white-space: nowrap;
    color: var(--nav-text); font-size: 8.8px; font-weight: 600; letter-spacing: .2px;
  }
  .vocab-list .is-current { color: var(--accent); }
  .vocab-list .stage-heading { color: #eef0f2; font-weight: 700; }

  .word-card {
    position: absolute; left: 274px; top: 102px; width: 804px; height: 595px;
    background: var(--card); border-radius: 25px 25px 0 25px;
  }
  .word-title {
    position: absolute; left: 0; right: 0; top: 49px; text-align: center;
    font-size: 14px; font-weight: 800; color: var(--ink);
  }
  .word-title svg { vertical-align: -2px; margin-left: 3px; }

  .review-steps { position: absolute; left: 160px; top: 98px; width: 489px; height: 28px; }
  .review-steps .connector { position: absolute; top: 14px; height: 1px; background: var(--step-line); width: 31px; }
  .review-step {
    position: absolute; top: 0; width: 98px; height: 28px; border-radius: 14px;
    display: flex; align-items: center; justify-content: center; gap: 7px;
    font-size: 9px; font-weight: 600; background: #fff;
  }
  .review-step--done { border: 1px solid var(--step-done); color: var(--step-done); }
  .review-step--current { background: #3a3a3a; color: #fff; border: 1px solid #3a3a3a; }
  .review-step--upcoming { border: 1px solid #d4d6d9; color: #8e9195; }

  .word-description {
    position: absolute; left: 32px; top: 157px; width: 712px;
    font-size: 9.7px; line-height: 12px; color: var(--ink-soft);
  }
  .word-description b { color: var(--ink); font-weight: 800; }

  .chart-title {
    position: absolute; left: 0; right: 0; top: 243px; text-align: center;
    font-size: 9.4px; font-weight: 800; color: var(--ink);
  }
  .learning-chart { position: absolute; left: 25px; top: 263px; }
  .learning-chart text { font-family: Arimo, Arial, sans-serif; }

  .analysis-title {
    position: absolute; left: 32px; top: 476px; font-size: 9.4px; font-weight: 800; color: var(--ink);
  }
  .analysis-body {
    position: absolute; left: 32px; top: 497px; width: 744px;
    font-size: 9.7px; line-height: 12px; color: var(--ink-soft);
  }
</style>
</head>
<body>
<div class="app-shell">
  <header class="app-header">
    <svg class="menu-toggle" width="24" height="16" viewBox="0 0 24 16" aria-label="Menu">
      <g stroke="#e6e8eb" stroke-width="1.6" stroke-linecap="round">
        <line x1="1" y1="2" x2="22" y2="2"/><line x1="1" y1="8" x2="23" y2="8"/><line x1="1" y1="14" x2="17" y2="14"/>
      </g>
    </svg>
    <div class="app-title">QuillaVorn
      <svg width="8" height="5" viewBox="0 0 8 5"><path d="M1 1l3 3 3-3" fill="none" stroke="#e6e8eb" stroke-width="1"/></svg>
    </div>
    <div class="header-actions">
      <svg width="14" height="14" viewBox="0 0 24 24" aria-label="Settings"><path fill="#e6e8eb" d="M19.4 13a7.5 7.5 0 0 0 0-2l2.1-1.6-2-3.5-2.5 1a7.6 7.6 0 0 0-1.7-1L15 3h-4l-.4 2.9a7.6 7.6 0 0 0-1.7 1l-2.5-1-2 3.5L6.6 11a7.5 7.5 0 0 0 0 2l-2.1 1.6 2 3.5 2.5-1a7.6 7.6 0 0 0 1.7 1L11 21h4l.4-2.9a7.6 7.6 0 0 0 1.7-1l2.5 1 2-3.5zM13 15.5a3.5 3.5 0 1 1 0-7 3.5 3.5 0 0 1 0 7z" transform="translate(-1 0)"/></svg>
      <svg width="14" height="14" viewBox="0 0 24 24" aria-label="Tasks"><path d="M19 12v7a2 2 0 0 1-2 2H5a2 2 0 0 1-2-2V7a2 2 0 0 1 2-2h9" fill="none" stroke="#e6e8eb" stroke-width="2.4"/><path d="M8 11l4 4 10-11" fill="none" stroke="#e6e8eb" stroke-width="2.6"/></svg>
      <span style="display:flex;align-items:center;gap:2px">
        <svg width="14" height="14" viewBox="0 0 24 24" aria-label="Account"><circle cx="12" cy="12" r="10" fill="none" stroke="#e6e8eb" stroke-width="2"/><circle cx="12" cy="10" r="3.5" fill="#e6e8eb"/><path d="M5.5 18.5c1.5-2.5 4-3.5 6.5-3.5s5 1 6.5 3.5" fill="none" stroke="#e6e8eb" stroke-width="2"/></svg>
        <svg width="8" height="5" viewBox="0 0 8 5"><path d="M1 1l3 3 3-3" fill="none" stroke="#e6e8eb" stroke-width="1"/></svg>
      </span>
    </div>
  </header>

  <nav class="main-nav">
    <div class="main-nav__item main-nav__item--active">
      <svg width="12" height="12" viewBox="0 0 24 24"><path fill="#fff" d="M12 2L1 12h3v10h6v-6h4v6h6V12h3z"/></svg>QuillaVorn
    </div>
    <div class="main-nav__item">
      <svg width="12" height="12" viewBox="0 0 24 24"><path fill="#8d939a" d="M12 2l3 7 7 .6-5.3 4.7L18.3 22 12 18l-6.3 4 1.6-7.7L2 9.6 9 9z"/></svg>Daily English
    </div>
    <div class="main-nav__item">
      <svg width="12" height="12" viewBox="0 0 24 24"><path fill="#8d939a" d="M5 2h11v20H5zm2 3v2h2V5zm4 0v2h2V5zM7 9v2h2V9zm4 0v2h2V9zm-4 4v2h2v-2zm4 0v2h2v-2zM9 18v4h3v-4zm8-8h3v12h-3z"/></svg>Business
    </div>
  </nav>

  <section class="work-panel">
    <div class="vocab-tools">
      <div class="deck-select">
        <svg width="12" height="12" viewBox="0 0 24 24"><path fill="#e6e8eb" d="M12 2l10 5-10 5L2 7z"/><path fill="none" stroke="#e6e8eb" stroke-width="2" d="M2 12l10 5 10-5M2 17l10 5 10-5"/></svg>
        All
        <svg class="chev" width="8" height="5" viewBox="0 0 8 5"><path d="M1 1l3 3 3-3" fill="none" stroke="#e6e8eb" stroke-width="1.2"/></svg>
      </div>
      <div class="popout-btn">
        <svg width="11" height="11" viewBox="0 0 24 24"><path d="M10 3H3v18h18v-7" fill="none" stroke="#e6e8eb" stroke-width="3"/><path d="M14 3h7v7M21 3L11 13" fill="none" stroke="#e6e8eb" stroke-width="3"/></svg>
      </div>
    </div>

    <div class="stage-tab">
      <svg width="8" height="8" viewBox="0 0 10 10"><path d="M2 8L8 2M3 2h5v5" fill="none" stroke="#2b2b2b" stroke-width="1.3"/></svg>
      Short Term Memory
    </div>

    <ul class="vocab-list">
      <li class="is-current" style="top:0">Grab</li>
      <li class="stage-heading" style="top:43px">Working Memory</li>
      <li style="top:80px">Cool Down</li>
      <li style="top:104px">Crave</li>
      <li style="top:129px">Go For</li>
      <li style="top:153px">Go-To</li>
      <li style="top:178px">In The Mood For</li>
      <li style="top:203px">Sip</li>
      <li style="top:227px">Soothing</li>
      <li style="top:252px">Stick With</li>
      <li style="top:276px">Throw In/Throw On</li>
      <li class="stage-heading" style="top:319px">Long-Term Memory</li>
      <li style="top:356px">Give It A Try</li>
    </ul>
  </section>

  <main class="word-card">
    <h1 class="word-title">Grab
      <svg width="15" height="15" viewBox="0 0 24 24"><path fill="var(--star)" d="M12 1.5l3.2 7 7.6.8-5.7 5.1 1.6 7.6L12 18.1 5.3 22l1.6-7.6L1.2 9.3l7.6-.8z"/></svg>
    </h1>

    <div class="review-steps">
      <span class="connector" style="left:98px"></span>
      <span class="connector" style="left:227px"></span>
      <span class="connector" style="left:356px"></span>
      <div class="review-step review-step--done" style="left:0">
        <svg width="12" height="12" viewBox="0 0 12 12"><circle cx="6" cy="6" r="6" fill="var(--step-done)"/><path d="M3.3 6.2l1.8 1.7 3.6-3.6" fill="none" stroke="#fff" stroke-width="1.3"/></svg>Review 1
      </div>
      <div class="review-step review-step--current" style="left:129px">
        <svg width="12" height="12" viewBox="0 0 12 12"><circle cx="6" cy="6" r="6" fill="#fff"/><path d="M3.3 6.2l1.8 1.7 3.6-3.6" fill="none" stroke="#3a3a3a" stroke-width="1.3"/></svg>Review 2
      </div>
      <div class="review-step review-step--upcoming" style="left:258px">
        <svg width="12" height="12" viewBox="0 0 12 12"><circle cx="6" cy="6" r="6" fill="var(--step-idle)"/><path d="M3.3 6.2l1.8 1.7 3.6-3.6" fill="none" stroke="#fff" stroke-width="1.3"/></svg>Review 3
      </div>
      <div class="review-step review-step--upcoming" style="left:387px">
        <svg width="12" height="12" viewBox="0 0 12 12"><circle cx="6" cy="6" r="6" fill="var(--step-idle)"/><path d="M3.3 6.2l1.8 1.7 3.6-3.6" fill="none" stroke="#fff" stroke-width="1.3"/></svg>Review 4
      </div>
    </div>

    <p class="word-description">The word "<b>grab</b>" is the most commonly used as a <b>verb</b>, meaning <b>to take something quickly or suddenly</b>. Imagine you're running late for school. You don't have time for breakfast, so you quickly <b>grab</b> an apple from the kitchen and rush out the door. As you reach the bus stop, your friend waves and says. "Hey, let's <b>grab</b> a coffee after class". Later, when you sit down, your phone starts ringing. You <b>grab</b> it from your bag and answer.</p>

    <h2 class="chart-title">Learning Curve Graph</h2>

    <svg class="learning-chart" width="750" height="170" viewBox="0 0 750 170" role="img" aria-label="Learning curve bar chart of reviews on 18 and 19 May">
      <rect x="6" y="8" width="733" height="32" fill="var(--band-long)"/>
      <rect x="6" y="40" width="733" height="64" fill="var(--band-working)"/>
      <rect x="6" y="104" width="733" height="16" fill="var(--band-short)"/>
      <rect x="6" y="120" width="733" height="17" fill="var(--band-forgotten)"/>
      <g font-size="6" fill="#666">
        <text x="14" y="26">Long-Term Memory</text>
        <text x="14" y="73">Working Memory</text>
        <text x="14" y="113">Short-Term Memory</text>
        <text x="14" y="129">Forgotten Memory</text>
      </g>
      <rect x="73" y="109" width="12" height="28" fill="var(--bar)"/>
      <rect x="145" y="40" width="14" height="97" fill="var(--bar)"/>
      <path d="M88 106 C110 110 130 120 145 136" fill="none" stroke="#555" stroke-width="1" stroke-dasharray="1 2.5"/>
      <path d="M159 41 C190 45 215 46 235 60 C260 80 280 110 297 136" fill="none" stroke="#555" stroke-width="1" stroke-dasharray="1 2.5"/>
      <g font-size="5.6" font-weight="700" fill="#222">
        <rect x="53" y="96" width="35" height="14" fill="#fff" stroke="#ddd" stroke-width=".6"/>
        <text x="70.5" y="105.5" text-anchor="middle">May 18</text>
        <rect x="117" y="31" width="36" height="15" fill="#fff" stroke="#ddd" stroke-width=".6"/>
        <text x="135" y="41" text-anchor="middle">May 19</text>
      </g>
      <line x1="6" y1="137" x2="746" y2="137" stroke="#444" stroke-width=".8"/>
      <g stroke="#444" stroke-width=".7">
        <line x1="13" y1="137" x2="13" y2="142"/><line x1="49.6" y1="137" x2="49.6" y2="142"/><line x1="86.2" y1="137" x2="86.2" y2="142"/><line x1="122.8" y1="137" x2="122.8" y2="142"/><line x1="159.4" y1="137" x2="159.4" y2="142"/><line x1="196" y1="137" x2="196" y2="142"/><line x1="232.6" y1="137" x2="232.6" y2="142"/><line x1="269.2" y1="137" x2="269.2" y2="142"/><line x1="305.8" y1="137" x2="305.8" y2="142"/><line x1="342.4" y1="137" x2="342.4" y2="142"/><line x1="379" y1="137" x2="379" y2="142"/><line x1="415.6" y1="137" x2="415.6" y2="142"/><line x1="452.2" y1="137" x2="452.2" y2="142"/><line x1="488.8" y1="137" x2="488.8" y2="142"/><line x1="525.4" y1="137" x2="525.4" y2="142"/><line x1="562" y1="137" x2="562" y2="142"/><line x1="598.6" y1="137" x2="598.6" y2="142"/><line x1="635.2" y1="137" x2="635.2" y2="142"/><line x1="671.8" y1="137" x2="671.8" y2="142"/><line x1="708.4" y1="137" x2="708.4" y2="142"/><line x1="745" y1="137" x2="745" y2="142"/>
      </g>
      <g font-size="6" fill="#222" text-anchor="middle">
        <text x="18" y="152">18 May</text><text x="49.6" y="152">12:00</text><text x="86.2" y="152">19 May</text><text x="122.8" y="152">12:00</text><text x="159.4" y="152">20 May</text><text x="196" y="152">12:00</text><text x="232.6" y="152">21 May</text><text x="269.2" y="152">12:00</text><text x="305.8" y="152">22 May</text><text x="342.4" y="152">12:00</text><text x="379" y="152">23 May</text><text x="415.6" y="152">12:00</text><text x="452.2" y="152">24 May</text><text x="488.8" y="152">12:00</text><text x="525.4" y="152">25 May</text><text x="562" y="152">12:00</text><text x="598.6" y="152">26 May</text><text x="635.2" y="152">12:00</text><text x="671.8" y="152">27 May</text><text x="708.4" y="152">12:00</text><text x="739" y="152">28 ...</text>
        <text x="377" y="162" font-weight="700">Date Range</text>
      </g>
    </svg>

    <h2 class="analysis-title">QuillaVorn Learning Analysis</h2>
    <p class="analysis-body">Lorem ipsum dolor sit amet, consectetur adipiscing elit, sed do eiusmod tempor incididunt ut labore et dolore magna aliqua. Ut enim ad minim veniam, quis nostru exercitation ullamco laboris nisi ut aliquip ex ea commodo consequat. Duis aute irure dolor in reprehenderit in voluptate velit esse cillum dolore eu fugiat nulla pari atur. Excepteur sint occaecat cupidatat non proident, sunt in culpa qui officia deserunt mollit anim id est laborum.</p>
  </main>
</div>
</body>
</html>
```